Marlow Landscaping Landing Page

I require a landing page for my landscaping business.

My business plan revolves around hooking clients with weeding services. Not lawn herbicide sprays, but actual hand weeding and bed maintenance. I've found my niche as most people do not want to do this kind of work. From there I often upsell clients into actual hardscaping or softscaping.

I like things to be clean, concise, and to the point. Not overly flashy, but not so minimal that that it's boring. My logo is a very good example of what I like.

The business is LGBTQ owned and operated. I do not broadcast this but I feel the logo itself, along with the name is usually enough to tip people into assumption. I'm not opposed to color, but I do not want the page to scream "gay". My favourite color is yellow...

I used to be a door to door salesman so I'm doing something different where I want to do all my selling in my first meeting with the client. With this said I do not need a section for "work pictures", as I have photos of my work on my tablet, which I show the client during the consultation.

Ideally i'd like my web site to actually be just a landing page. I'd like room for all the following information within the page;

- description of services;
Weeding of Perennial and Flower Beds
Selective Pruning of Trees and Shrubs
Hedging
Landscape Construction
Landscape Design
Total Lawn Treatment Plans
Landscape Pest Control

- contact information, phone, email
Gerald Hanswick
204-731-4426
ger.hanswick@brelvanyard.com

- "free estimates" somewhere on the page that is either led to by the eye, or very easy to notice and see

- and my slogan which is "dependable, reliable, consistent"

- room for a link to my future ratewell account so they can see reviews from real people

- My Logo present

Any or all of these can be custom made graphics or simply text, whatever looks best

I do not want people to have to search for information throughout. Design it in such a way that either the eye flows naturally from one piece of information to the other, or that it's all compartmentalized neatly enough that everything is easy to find.

As I am a landscape and outdoor maintenance service I'm no opposed to images such as flowers, trees, landscaping, etc being present. However please note that my main focus and source of income comes from weeding services, everything else is bonus cash.

Many of my clients are extremely wealthy individuals who pay over $1000 for the season for me just to show up and pull weeds. So making the website appeal to wealthy people as opposed to the average joe is paramount.

I do not cut grass. Please do not have any indication on the website, either through writing or graphics that implies that I cut grass. There are enough companies doing that.

Target Market(s)

Wealthy, often elderly individuals.

Industry/Entity Type

Landscape Gardening

Coding

Coded - Design and coding required

Number of Pages Required

1 page

Font styles to use
Sans Serif

Colors

Designer to choose colors to be used in the design.

Requirements
Must have
• - description of services;
• Weeding of Perennial and Flower Beds
• Selective Pruning of Trees and Shrubs
• Hedging
• Landscape Construction
• Landscape Design
• Total Lawn Treatment Plans
• Landscape Pest Control
• - contact information, phone, email
• Gerald Hanswick
• 204-731-4426
• ger.hanswick@brelvanyard.com
• - "free estimates" somewhere on the page that is either led to by the eye, or very easy to notice and see
• - and my slogan which is "dependable, reliable, consistent"
• - room for a link to my future ratewell account so they can see reviews from real people
• - My Logo present
Nice to have
• Flowers or weeds depicted. Possibly some hardscaping and softscaping if it doesnt look too bulky and crowded.
Should not have
• grass

```html
<!DOCTYPE html>
<html lang="en">
<head>
<meta charset="utf-8">
<title>Marlow Landscaping</title>
<link rel="stylesheet" href="https://fonts.googleapis.com/css2?family=Raleway:wght@300;400;500;600;700;800&family=Lobster&display=swap">
<style>
:root{
  --sky-top:#a9ecee;
  --sky-mid:#c4f1f0;
  --meadow:#dff3b8;
  --white:#ffffff;
  --ink:#111111;
  --text-grey:#8a8a8a;
  --accent-red:#e8242c;
  --frame-red:#c8171b;
  --orange:#f07f1e;
  --yellow:#ffd23a;
  --field-border:#d2d2d2;
  --panel-grey:#f0f0f0;
  --leaf-green:#4c8b2b;
}
*{box-sizing:border-box;margin:0;padding:0}
html,body{width:1200px;height:768px;overflow:hidden}
body{
  position:relative;
  font-family:'Raleway',sans-serif;
  background:
    radial-gradient(ellipse 600px 120px at 300px 210px,rgba(255,255,255,.45),transparent 70%),
    radial-gradient(ellipse 500px 90px at 900px 230px,rgba(255,255,255,.4),transparent 70%),
    linear-gradient(180deg,var(--sky-top) 0%,var(--sky-mid) 45%,#e6f7e0 70%,var(--meadow) 100%);
}
.logo-card{
  position:absolute;left:30px;top:45px;width:568px;height:111px;
  background:var(--white);
  box-shadow:0 8px 6px -4px rgba(0,0,0,.25);
  display:flex;align-items:center;justify-content:center;gap:14px;
}
.logo-card .logo-dot{width:34px;height:34px;border-radius:50%;background:var(--yellow)}
.logo-card .logo-name{font-weight:600;font-size:44px;letter-spacing:-1px;color:#222;text-transform:uppercase}
.contact-block{position:absolute;left:695px;top:46px;color:var(--ink)}
.contact-block .lead{font-size:14px;font-weight:500}
.contact-block .owner{font-size:19px;font-weight:700;color:var(--accent-red);text-transform:uppercase;margin-top:3px}
.phone-box{
  margin-top:6px;width:231px;height:45px;border:2px solid var(--ink);
  display:flex;align-items:center;gap:14px;padding-left:4px;
}
.phone-box .icon{width:34px;height:34px;background:var(--ink);border-radius:6px;display:flex;align-items:center;justify-content:center}
.phone-box .number{font-weight:800;font-size:22px;letter-spacing:.5px}
.contact-block .email{display:flex;align-items:center;gap:8px;font-size:14px;margin-top:6px}
.reviews-link{
  position:absolute;left:996px;top:38px;display:flex;align-items:center;gap:8px;
  font-size:14px;font-weight:500;color:var(--ink);text-decoration:none;
}
.reviews-link .badge{width:28px;height:28px;background:var(--accent-red);border-radius:3px}
.estimates-btn{
  position:absolute;left:939px;top:68px;width:231px;height:88px;
  background:var(--orange);border:2px solid #d86a10;
  box-shadow:0 3px 6px rgba(0,0,0,.25);
  color:var(--white);text-decoration:none;padding:10px 0 0 18px;
}
.estimates-btn .small{font-family:'Lobster',cursive;font-size:21px;display:block;color:#fff3e0}
.estimates-btn .big{font-weight:800;font-size:32px;text-transform:uppercase;display:block;margin-top:-2px}
.main-panel{
  position:absolute;left:30px;top:244px;width:1142px;height:560px;
  background:var(--white);border-radius:3px;
  box-shadow:0 0 4px rgba(0,0,0,.1);
}
.photo-frame{
  position:absolute;left:18px;top:23px;width:313px;height:379px;
  border:1px solid #ddd;background:var(--white);
  box-shadow:0 1px 4px rgba(0,0,0,.12);padding:10px;
}
.photo-frame .photo{
  width:100%;height:100%;
  background:linear-gradient(160deg,#6f8f3c 0%,#4d7a2a 40%,#e6b820 60%,#5f7b36 80%,#7d6a43 100%);
}
.intro{position:absolute;left:357px;top:50px;width:480px}
.slogan{font-family:'Lobster',cursive;font-weight:400;font-size:32px;color:var(--ink);line-height:1.1}
.subhead{font-size:17px;font-weight:500;text-transform:uppercase;color:var(--ink);margin-top:8px}
.intro p{font-size:16.5px;line-height:30px;color:var(--text-grey);margin-top:10px;font-weight:400}
.contact-cta{
  position:absolute;left:359px;top:305px;width:192px;height:88px;
  background:var(--accent-red);border-radius:2px;
  box-shadow:0 2px 5px rgba(0,0,0,.35);text-decoration:none;
  padding:18px 0 0 20px;
}
.contact-cta .big{display:block;color:var(--white);font-weight:800;font-size:24px;text-transform:uppercase}
.contact-cta .small{display:block;color:var(--yellow);font-family:'Lobster',cursive;font-size:19px;margin-top:2px}
.cta-arrow{position:absolute;left:571px;top:328px}
.services-title{position:absolute;left:20px;top:478px;font-family:'Lobster',cursive;font-weight:400;font-size:36px;color:var(--ink)}
.contact-form{
  position:absolute;left:833px;top:43px;width:289px;height:540px;
  border:7px solid var(--frame-red);background:var(--panel-grey);
  padding:22px 13px 0 13px;
}
.contact-form .kicker{font-family:'Lobster',cursive;font-size:17px;color:#333}
.contact-form h2{font-size:31px;font-weight:700;text-transform:uppercase;color:var(--ink);margin-top:0;line-height:1.1}
.contact-form .hatch{
  height:6px;margin:8px 0 18px;
  background:repeating-linear-gradient(135deg,#bbb 0 1px,transparent 1px 3px);
}
.contact-form .field{
  display:block;width:248px;height:56px;margin-bottom:15px;
  background:var(--white);border:3px solid var(--field-border);
  font-family:'Raleway',sans-serif;font-size:16px;color:#777;padding:0 11px;
}
.contact-form textarea.field{height:90px;padding-top:16px;resize:none}
</style>
</head>
<body>
  <header>
    <div class="logo-card">
      <span class="logo-dot"></span>
      <span class="logo-name">Marlow Landscaping</span>
    </div>

    <div class="contact-block">
      <div class="lead">Get In Touch with</div>
      <div class="owner">Gerald Hanswick</div>
      <div class="phone-box">
        <span class="icon">
          <svg width="22" height="22" viewBox="0 0 24 24"><path fill="#fff" d="M6.6 10.8a15.1 15.1 0 0 0 6.6 6.6l2.2-2.2c.3-.3.7-.4 1-.2 1.1.4 2.3.6 3.6.6.6 0 1 .4 1 1V20c0 .6-.4 1-1 1A17 17 0 0 1 3 4c0-.6.4-1 1-1h3.5c.6 0 1 .4 1 1 0 1.2.2 2.4.6 3.6.1.3 0 .7-.2 1l-2.3 2.2z"/></svg>
        </span>
        <span class="number">204-731-4426</span>
      </div>
      <div class="email">
        <svg width="14" height="10" viewBox="0 0 14 10"><rect x="0.5" y="0.5" width="13" height="9" fill="#111"/><path d="M1 1l6 5 6-5" stroke="#fff" stroke-width="1.2" fill="none"/></svg>
        <span>ger.hanswick@brelvanyard.com</span>
      </div>
    </div>

    <a class="reviews-link" href="#">See Reviews on RATEWELL <span class="badge"></span></a>

    <a class="estimates-btn" href="#">
      <span class="small">Click Here to Get Free</span>
      <span class="big">Estimates</span>
    </a>
  </header>

  <main class="main-panel">
    <div class="photo-frame">
      <div class="photo" role="img" aria-label="Gloved hand pulling weeds from a garden bed"></div>
    </div>

    <section class="intro">
      <h1 class="slogan">Dependable, Reliable &amp; Consistent</h1>
      <div class="subhead">Landscape and outdoor maintenance services!</div>
      <p>Lorem Ipsum is simply dummy text of the printing and typesetting industry. Lorem Ipsum has been the industry's standard dummy text ever since the 1500s, when an unknown printer took a galley of type and scrambled it to make a type specimen book.</p>
    </section>

    <a class="contact-cta" href="#">
      <span class="big">Contact Us</span>
      <span class="small">To Know More</span>
    </a>

    <svg class="cta-arrow" width="130" height="40" viewBox="0 0 130 40">
      <path d="M4 36 C30 10 70 4 118 14" stroke="#c8171b" stroke-width="3.5" fill="none" stroke-linecap="round"/>
      <path d="M104 4 L122 15 L106 26" stroke="#c8171b" stroke-width="3.5" fill="none" stroke-linecap="round" stroke-linejoin="round"/>
    </svg>

    <h2 class="services-title">Our Services</h2>

    <form class="contact-form">
      <div class="kicker">Lorem Ipsum is simply dummy text</div>
      <h2>Contact Us</h2>
      <div class="hatch"></div>
      <input class="field" type="text" placeholder="Name:">
      <input class="field" type="email" placeholder="Email:">
      <input class="field" type="tel" placeholder="Phone:">
      <input class="field" type="text" placeholder="Location:">
      <textarea class="field" placeholder="Message:"></textarea>
    </form>
  </main>
</body>
</html>
```